Business Card Design Project

We have recently completed MakerHive projects for a new logo and wesbite.
We now require new business cards.
We hand out very little printed material to clients as all information is online. When we do hand out something, like a business card, we want it to have real impact and make a statement about the quality and professionalism of our company.
We have an idea of what we want our card to look like but we want a designer to make sure they have impact and look great.
Our requirements are…
Size: 85mm X 55mm - Landscape
Front of card: Logo plus the following contact information.
Derek Fenwick
Operations Manager
Phone +44(0) 1632 xxx xxx
Mobile +44(0) 7700 xxx xxx
Email derekf@corebitsys.example
Address 19 Tarlow Street, Aberdeen AB12 4QP
Website www.corebitsys.example
How you layout the front of the card is up to you, we would like to see some different ideas. Attached are two versions of our logo that may be used.
Back of card: We would like this to be simple but again have impact. Our current thought is to have the logo or just the large W design from the logo in white against a dark background, perhaps made up from the dark green in the logo.
The logos are attached so you can see the colours in them but the dark ones are..
Dark Blue = C:88, M:55, Y:44, K:28
Dark Green = C:87, M:53, Y:50, K:50
We sometimes also use a bright orange as an accent or highlight colour…
Orange: = C:0, M:39, Y:94, K:0

```html
<!DOCTYPE html>
<html lang="en">
<head>
<meta charset="utf-8">
<title>Corebit Systems – Business Cards</title>
<link rel="stylesheet" href="https://fonts.googleapis.com/css2?family=Oswald:wght@500;600&family=Roboto+Condensed:wght@400;700&display=swap">
<style>
  :root {
    --page-bg: #d9dcdd;
    --teal-dark: #1d3f4c;
    --teal-mid: #2b5a69;
    --teal-light: #4a7e8c;
    --band-teal: #264f5e;
    --card-white: #ffffff;
    --ink-white: #ffffff;
    --ink-soft: rgba(255,255,255,0.85);
    --logo-ink: #1f4755;
  }
  * { box-sizing: border-box; margin: 0; padding: 0; }
  html, body {
    width: 1200px; height: 900px; overflow: hidden;
    background: var(--page-bg);
  }
  .canvas {
    width: 1200px; height: 900px;
    display: flex; align-items: center; justify-content: center; gap: 40px;
  }
  .card {
    width: 540px; height: 350px;
    position: relative; overflow: hidden;
    box-shadow: 0 6px 18px rgba(0,0,0,0.18);
  }

  /* Front: contact side */
  .card-front {
    background:
      radial-gradient(ellipse 70% 80% at 28% 22%, var(--teal-light) 0%, transparent 70%),
      linear-gradient(135deg, var(--teal-mid) 0%, var(--teal-dark) 100%);
    color: var(--ink-white);
  }
  .front-brand {
    position: absolute; left: 34px; top: 58px;
    display: flex; align-items: center; gap: 10px;
    font-family: "Oswald", sans-serif; font-weight: 600;
    font-size: 27px; letter-spacing: 1px; color: var(--ink-white);
  }
  .brand-dot {
    width: 14px; height: 14px; border-radius: 50%; background: var(--ink-white);
  }
  .front-divider {
    position: absolute; left: 262px; top: 120px; width: 1px; height: 190px;
    background: rgba(255,255,255,0.35);
  }
  .contact {
    position: absolute; left: 284px; top: 112px; right: 20px;
  }
  .contact-name {
    font-family: "Oswald", sans-serif; font-weight: 600;
    font-size: 30px; line-height: 1; letter-spacing: 0.5px;
  }
  .contact-title {
    font-family: "Roboto Condensed", sans-serif; font-weight: 700;
    font-size: 12px; letter-spacing: 1.5px; margin-top: 6px; color: var(--ink-soft);
  }
  .contact-list { list-style: none; margin-top: 18px; }
  .contact-list li {
    display: flex; align-items: center; gap: 10px;
    font-family: "Roboto Condensed", sans-serif; font-size: 12.5px;
    color: var(--ink-soft); height: 22px; white-space: nowrap;
  }
  .contact-list svg { width: 13px; height: 13px; flex: none; fill: var(--ink-white); }

  /* Back: brand side */
  .card-back { background: var(--card-white); }
  .back-brand {
    position: absolute; left: 0; right: 0; top: 110px;
    display: flex; align-items: center; justify-content: center; gap: 12px;
    font-family: "Oswald", sans-serif; font-weight: 600;
    font-size: 38px; letter-spacing: 1.5px; color: var(--logo-ink);
  }
  .back-brand .brand-dot { width: 18px; height: 18px; background: var(--logo-ink); }
  .back-band {
    position: absolute; left: 0; right: 0; top: 218px; height: 30px;
    background: var(--band-teal);
    display: flex; align-items: center; padding-left: 34px;
    font-family: "Roboto Condensed", sans-serif; font-weight: 700;
    font-size: 13px; letter-spacing: 2.5px; color: var(--ink-white);
  }
</style>
</head>
<body>
<main class="canvas">

  <section class="card card-front" aria-label="Business card, contact side">
    <div class="front-brand"><span class="brand-dot"></span>COREBIT SYSTEMS</div>
    <div class="front-divider"></div>
    <div class="contact">
      <h1 class="contact-name">Derek Fenwick</h1>
      <p class="contact-title">OPERATIONS MANAGER</p>
      <ul class="contact-list">
        <li>
          <svg viewBox="0 0 24 24" aria-hidden="true"><path d="M6.6 10.8a15.1 15.1 0 0 0 6.6 6.6l2.2-2.2c.3-.3.7-.4 1-.2 1.1.4 2.3.6 3.6.6.6 0 1 .4 1 1V20c0 .6-.4 1-1 1A17 17 0 0 1 3 4c0-.6.4-1 1-1h3.5c.6 0 1 .4 1 1 0 1.3.2 2.5.6 3.6.1.3 0 .7-.2 1z"/></svg>
          +44(0) 1632 xxx xxx
        </li>
        <li>
          <svg viewBox="0 0 24 24" aria-hidden="true"><path d="M7 1h10a2 2 0 0 1 2 2v18a2 2 0 0 1-2 2H7a2 2 0 0 1-2-2V3a2 2 0 0 1 2-2zm0 3v14h10V4zm5 15.5a1.2 1.2 0 1 0 0 2.4 1.2 1.2 0 0 0 0-2.4z"/></svg>
          +44(0) 7700 xxx xxx
        </li>
        <li>
          <svg viewBox="0 0 24 24" aria-hidden="true"><path d="M2 5h20v14H2zm2 2v.5l8 5 8-5V7zm0 2.8V17h16V9.8l-8 5z"/></svg>
          derekf@corebitsys.example
        </li>
        <li>
          <svg viewBox="0 0 24 24" aria-hidden="true"><path d="M12 2a10 10 0 1 0 0 20 10 10 0 0 0 0-20zm6.9 9h-3a15 15 0 0 0-1.3-5.6A8 8 0 0 1 18.9 11zM12 4.1c.9 1.2 1.8 3.5 1.9 6.9h-3.8c.1-3.4 1-5.7 1.9-6.9zM9.4 5.4A15 15 0 0 0 8.1 11h-3a8 8 0 0 1 4.3-5.6zM5.1 13h3a15 15 0 0 0 1.3 5.6A8 8 0 0 1 5.1 13zm6.9 6.9c-.9-1.2-1.8-3.5-1.9-6.9h3.8c-.1 3.4-1 5.7-1.9 6.9zm2.6-1.3a15 15 0 0 0 1.3-5.6h3a8 8 0 0 1-4.3 5.6z"/></svg>
          www.corebitsys.example
        </li>
        <li>
          <svg viewBox="0 0 24 24" aria-hidden="true"><path d="M12 2a7 7 0 0 0-7 7c0 5.2 7 13 7 13s7-7.8 7-13a7 7 0 0 0-7-7zm0 9.5a2.5 2.5 0 1 1 0-5 2.5 2.5 0 0 1 0 5z"/></svg>
          19 Tarlow Street, Aberdeen AB12 4QP
        </li>
      </ul>
    </div>
  </section>

  <section class="card card-back" aria-label="Business card, brand side">
    <div class="back-brand"><span class="brand-dot"></span>COREBIT SYSTEMS</div>
    <div class="back-band">WWW.COREBITSYS.EXAMPLE</div>
  </section>

</main>
</body>
</html>
```